Architectural Design Build company needs a direct mail flyer

We are a fully service Design Build company who specialize in luxury custom and pre-designed new homes and major home renovations. Our team consists of seasoned architectural, interior design and general contracting professionals all under one roof. We offer clients a transparent, streamlined process to maximize their investment and completion on a timely basis. Leveraging photography and a few before and after and also our Best Builder Awards.

Target Market(s)

Homeowners and buyers between 40-60 years old and financial investment of $300k or more for renovations and $1,000,000 or more for new construction.

Industry/Entity Type

homebuilding and renovations

Colors

Designer to choose colors to be used in the design.

Requirements
Must have
• The construction segments we are focusing this mailer on are transformative renovations and professionally designed custom new homes. . Should have the Pelbrook Before kitchen and after as well as the exterior before and after. and new construction elevation photos.
Nice to have
• WOuld like to see two befores and afters highlighted, mention that are architect and designer are part of the team from start to finish,

```html
<!DOCTYPE html>
<html lang="en">
<head>
<meta charset="utf-8">
<title>Pelbrook Design Build – Direct Mail Flyer</title>
<link rel="stylesheet" href="https://fonts.googleapis.com/css2?family=Archivo:wght@500;700;800;900&family=Arimo:wght@400;700&display=swap">
<style>
:root{
  --lime:#d8e36b;
  --ink:#2a2624;
  --paper:#ffffff;
  --stage:#2b2e33;
  --muted:#55504c;
}
*{box-sizing:border-box;margin:0;padding:0}
html,body{width:1200px;height:836px;overflow:hidden;background:var(--stage)}
body{position:relative;font-family:"Arimo",Arial,sans-serif;color:var(--ink)}
.page{position:absolute;top:28px;width:552px;height:780px;background:var(--paper);overflow:hidden}
.page--process{left:32px}
.page--strong{left:616px}
.abs{position:absolute}
.photo{position:absolute;border-radius:10px;overflow:hidden}
.photo-tag{position:absolute;top:0;left:0;background:var(--lime);color:var(--ink);font-family:"Archivo",Arial,sans-serif;font-weight:800;font-size:13px;padding:3px 10px}

/* Process page */
.logo-box{left:118px;top:22px;width:170px;height:50px;background:var(--lime);display:flex;align-items:center;justify-content:center;font-family:"Archivo",Arial,sans-serif;font-weight:900;font-size:24px;letter-spacing:2px;color:var(--ink)}
.accent-line{left:370px;top:86px;width:170px;height:5px;background:var(--lime)}
.title{left:60px;top:90px;font-family:"Archivo",Arial,sans-serif;line-height:.9}
.title__the{font-weight:800;font-size:19px}
.title__brand{font-weight:900;font-size:42px;color:var(--lime);letter-spacing:-1px}
.title__process{font-weight:900;font-size:50px;letter-spacing:-2px}
.title__tag{display:inline-block;margin-top:6px;background:var(--lime);font-family:"Archivo",Arial,sans-serif;font-weight:500;font-size:12px;padding:3px 8px}
.owners-photo{left:340px;top:104px;width:190px;height:208px;border-radius:0;background:linear-gradient(180deg,#f3f1ee 0%,#ddd6d0 55%,#3a3532 56%,#2a2624 100%);z-index:2}
.about-band{left:0;top:262px;width:552px;height:200px;background:var(--ink);color:var(--paper)}
.about-band h2{position:absolute;left:40px;top:22px;font-family:"Archivo",Arial,sans-serif;font-weight:800;font-size:22px;border-bottom:3px solid var(--lime);line-height:1.1}
.about-band p{position:absolute;left:40px;top:70px;width:470px;font-size:12.5px;line-height:1.6}
.services-pill{left:0;top:440px;height:38px;padding:0 26px 0 36px;background:var(--lime);border-radius:0 20px 20px 0;display:flex;align-items:center;font-family:"Archivo",Arial,sans-serif;font-weight:800;font-size:19px;z-index:3}
.services{left:20px;top:490px;width:516px;display:grid;grid-template-columns:repeat(3,1fr);row-gap:12px}
.service{padding:0 8px;border-left:1px solid #9a948f}
.service:nth-child(3n+1){border-left:none;padding-left:0}
.service__name{display:flex;align-items:center;gap:5px;font-family:"Archivo",Arial,sans-serif;font-weight:800;font-size:12px;white-space:nowrap}
.service__name svg{flex:none}
.service__time{font-size:9.5px;margin:2px 0 3px 19px;color:var(--muted)}
.service__text{font-size:9px;line-height:1.3;margin-left:19px}
.footer{left:0;top:722px;width:552px;height:58px;background:var(--lime);display:flex;align-items:center;justify-content:space-around;font-size:12px}
.contact{display:flex;align-items:center;gap:7px}
.contact svg{flex:none}

/* Strong page */
.strong-band{left:0;top:0;width:552px;height:62px;background:var(--ink)}
.strong-band__title{position:absolute;left:28px;top:18px;font-family:"Archivo",Arial,sans-serif;font-weight:800;font-size:22px;color:var(--lime);letter-spacing:1px}
.strong-band__logo{position:absolute;right:28px;top:16px;font-family:"Archivo",Arial,sans-serif;font-weight:900;font-size:24px;color:var(--lime);letter-spacing:2px}
.strong-heading{left:28px;top:78px;font-family:"Archivo",Arial,sans-serif;font-weight:800;font-size:22px}
.strong-intro{left:28px;top:112px;width:496px;font-size:12px;line-height:1.55}
.ext-before{left:24px;top:196px;width:236px;height:140px;background:linear-gradient(160deg,#9fb3c4 0%,#d8d2b8 45%,#5f7a45 100%);z-index:2;border:2px solid var(--ink)}
.ext-after{left:236px;top:236px;width:292px;height:190px;background:linear-gradient(160deg,#c7d6e2 0%,#f1efe9 45%,#4f8a3c 100%);z-index:2;border:2px solid var(--ink)}
.strong-mid{left:0;top:340px;width:552px;height:180px;background:var(--ink);color:var(--paper)}
.strong-mid p{position:absolute;left:28px;top:96px;width:496px;font-size:12px;line-height:1.55}
.kit-before{left:24px;top:532px;width:170px;height:86px;background:linear-gradient(150deg,#5a3a2a 0%,#7a5a44 55%,#b9b1a2 100%);border:2px solid var(--ink)}
.kit-after{left:24px;top:626px;width:170px;height:86px;background:linear-gradient(150deg,#f4f4f2 0%,#dcd8d0 55%,#7a5b3f 100%);border:2px solid var(--ink)}
.awards{left:214px;top:540px;width:318px;height:160px;display:flex;gap:12px}
.award{flex:1}
.footer--strong{justify-content:flex-end;gap:22px;padding-right:22px}
</style>
</head>
<body>

<section class="page page--process">
  <div class="abs logo-box">PELBROOK</div>
  <div class="abs accent-line"></div>

  <div class="abs title">
    <div class="title__the">THE</div>
    <div class="title__brand">PELBROOK</div>
    <div class="title__process">PROCESS</div>
    <div class="title__tag">Designed To Maximize Investment</div>
  </div>

  <div class="photo owners-photo" role="img" aria-label="Portrait of the two company owners standing with arms crossed, wearing black t-shirts"></div>

  <div class="abs about-band">
    <h2>About US:</h2>
    <p>At Pelbrook, our success is driven by the exceptional talent and dedication of our team. Led by owners Ardson Pelbrook, M. Eng., and Dane Morrow, both esteemed former pro league players, our diverse team brings together a wealth of experience and expertise. As a design/build company, Pelbrook seamlessly integrates design and construction services.</p>
  </div>

  <div class="abs services-pill">Our Services:</div>

  <div class="abs services">
    <div class="service">
      <div class="service__name"><svg width="14" height="14" viewBox="0 0 14 14"><circle cx="7" cy="7" r="6" fill="none" stroke="#2a2624" stroke-width="1.5"/><path d="M4 7l2 2 4-4" fill="none" stroke="#2a2624" stroke-width="1.6"/></svg>Initial Consultation</div>
      <div class="service__time">(1-2 Weeks)</div>
      <div class="service__text">We begin by understanding your vision, preferences, and functional needs, laying the foundation for a successful and meaningful project.</div>
    </div>
    <div class="service">
      <div class="service__name"><svg width="14" height="14" viewBox="0 0 14 14"><circle cx="7" cy="7" r="6" fill="none" stroke="#2a2624" stroke-width="1.5"/><path d="M4 7l2 2 4-4" fill="none" stroke="#2a2624" stroke-width="1.6"/></svg>Schematic Design</div>
      <div class="service__time">(1-2 Months)</div>
      <div class="service__text">Our architects and designers craft initial layouts and visual concepts, collaborating with you to align the design with your unique style.</div>
    </div>
    <div class="service">
      <div class="service__name"><svg width="14" height="14" viewBox="0 0 14 14"><circle cx="7" cy="7" r="6" fill="none" stroke="#2a2624" stroke-width="1.5"/><path d="M4 7l2 2 4-4" fill="none" stroke="#2a2624" stroke-width="1.6"/></svg>Design Development</div>
      <div class="service__time">(1-2 Months)</div>
      <div class="service__text">We transform initial ideas into detailed plans, refining materials, finishes, and functionality.</div>
    </div>
    <div class="service">
      <div class="service__name"><svg width="14" height="14" viewBox="0 0 14 14"><circle cx="7" cy="7" r="6" fill="none" stroke="#2a2624" stroke-width="1.5"/><path d="M4 7l2 2 4-4" fill="none" stroke="#2a2624" stroke-width="1.6"/></svg>Initial Consultation</div>
      <div class="service__time">(1-2 Weeks)</div>
      <div class="service__text">Finalized plans and specifications are meticulously reviewed to ensure every design detail is accounted for, setting the stage for flawless execution.</div>
    </div>
    <div class="service">
      <div class="service__name"><svg width="14" height="14" viewBox="0 0 14 14"><circle cx="7" cy="7" r="6" fill="none" stroke="#2a2624" stroke-width="1.5"/><path d="M4 7l2 2 4-4" fill="none" stroke="#2a2624" stroke-width="1.6"/></svg>Schematic Design</div>
      <div class="service__time">(1-2 Months)</div>
      <div class="service__text">We navigate the permitting process on your behalf, ensuring clear communication and minimizing potential delays to keep your project on track.</div>
    </div>
    <div class="service">
      <div class="service__name"><svg width="14" height="14" viewBox="0 0 14 14"><circle cx="7" cy="7" r="6" fill="none" stroke="#2a2624" stroke-width="1.5"/><path d="M4 7l2 2 4-4" fill="none" stroke="#2a2624" stroke-width="1.6"/></svg>Design Development</div>
      <div class="service__time">(1-2 Months)</div>
      <div class="service__text">We begin by understanding your vision, preferences, and functional needs, laying the foundation for a successful and meaningful project.</div>
    </div>
  </div>

  <div class="abs footer">
    <div class="contact"><svg width="18" height="18" viewBox="0 0 18 18"><circle cx="9" cy="9" r="9" fill="#2a2624"/><rect x="4.5" y="6" width="9" height="6.5" fill="none" stroke="#d8e36b" stroke-width="1"/><path d="M4.5 6l4.5 3.5 4.5-3.5" fill="none" stroke="#d8e36b" stroke-width="1"/></svg>hello@pelbrookbuild.com</div>
    <div class="contact"><svg width="18" height="18" viewBox="0 0 18 18"><circle cx="9" cy="9" r="9" fill="#2a2624"/><path d="M6 5l2 2-1 1.2c.6 1.3 1.5 2.2 2.8 2.8L11 10l2 2-1.3 1.3C8.5 13 5 9.5 4.7 6.3z" fill="#d8e36b"/></svg>+000 123 456 789</div>
    <div class="contact"><svg width="18" height="18" viewBox="0 0 18 18"><circle cx="9" cy="9" r="9" fill="#2a2624"/><circle cx="9" cy="9" r="5" fill="none" stroke="#d8e36b" stroke-width="1"/><path d="M4 9h10M9 4c-2.5 3-2.5 7 0 10M9 4c2.5 3 2.5 7 0 10" fill="none" stroke="#d8e36b" stroke-width="1"/></svg>www.yourwebsite.com</div>
  </div>
</section>

<section class="page page--strong">
  <div class="abs strong-band">
    <div class="strong-band__title">PELBROOKSTRONG</div>
    <div class="strong-band__logo">PELBROOK</div>
  </div>

  <h1 class="abs strong-heading">Resilient Homes Built To Endure</h1>
  <p class="abs strong-intro">In regions like Florida and Colorado, where extreme weather is a constant challenge, Pelbrook Design Build sets itself apart with its expertise in resilient construction. By focusing on reinforced foundations and materials that exceed building codes, Pelbrook creates homes that combine energy efficiency, durability, and architectural elegance.</p>

  <div class="abs strong-mid">
    <p>From hurricane-resistant roofing and moisture-proof materials in Florida to insulated siding and framing designed for Colorado’s harsh winters, every detail is thoughtfully engineered to withstand the elements. PELBROOKSTRONG represents the perfect balance of strength, efficiency, and design, ensuring that each home remains a secure and timeless investment.</p>
  </div>

  <div class="photo ext-before" role="img" aria-label="Exterior of a two-storey home with porch and palm trees before renovation"><span class="photo-tag">Before</span></div>
  <div class="photo ext-after" role="img" aria-label="Renovated white two-storey home with wraparound porch and new lawn after renovation"><span class="photo-tag">After</span></div>

  <div class="photo kit-before" role="img" aria-label="Kitchen with dark wood cabinets before renovation"><span class="photo-tag">Before</span></div>
  <div class="photo kit-after" role="img" aria-label="Bright white kitchen with island and range hood after renovation"><span class="photo-tag">After</span></div>

  <div class="abs awards">
    <svg class="award" viewBox="0 0 100 160" role="img" aria-label="Best home builder award badge, 2021"><polygon points="0,0 100,0 100,150 50,120 0,150" fill="#141414"/></svg>
    <svg class="award" viewBox="0 0 100 160" role="img" aria-label="Best home builder award badge, 2023"><polygon points="0,0 100,0 100,150 50,120 0,150" fill="#141414"/></svg>
    <svg class="award" viewBox="0 0 100 160" role="img" aria-label="Best of the city 2024 winner badge"><rect x="2" y="2" width="96" height="130" fill="#141414"/><rect x="14" y="20" width="72" height="100" fill="none" stroke="#ffffff" stroke-width="3"/></svg>
  </div>

  <div class="abs footer footer--strong">
    <div class="contact"><svg width="18" height="18" viewBox="0 0 18 18"><circle cx="9" cy="9" r="9" fill="#2a2624"/><rect x="4.5" y="6" width="9" height="6.5" fill="none" stroke="#d8e36b" stroke-width="1"/><path d="M4.5 6l4.5 3.5 4.5-3.5" fill="none" stroke="#d8e36b" stroke-width="1"/></svg>hello@pelbrookbuild.com</div>
    <div class="contact"><svg width="18" height="18" viewBox="0 0 18 18"><circle cx="9" cy="9" r="9" fill="#2a2624"/><path d="M6 5l2 2-1 1.2c.6 1.3 1.5 2.2 2.8 2.8L11 10l2 2-1.3 1.3C8.5 13 5 9.5 4.7 6.3z" fill="#d8e36b"/></svg>+000 123 456 789</div>
    <div class="contact"><svg width="18" height="18" viewBox="0 0 18 18"><circle cx="9" cy="9" r="9" fill="#2a2624"/><circle cx="9" cy="9" r="5" fill="none" stroke="#d8e36b" stroke-width="1"/><path d="M4 9h10M9 4c-2.5 3-2.5 7 0 10M9 4c2.5 3 2.5 7 0 10" fill="none" stroke="#d8e36b" stroke-width="1"/></svg>www.yourwebsite.com</div>
  </div>
</section>

</body>
</html>
```